2 sided Handyman Postcard Design with coupon on the back

Company name is "Merle Fixwise" Looking for a postcard that's also a business card. Showing Merle Fixwise, 4718 Quarry Bend Ln NW, Maple Hollow, Vermont 05999, 937-555-0148, mtolbert@fixwisemail.com coupon- $25 off any job over $100, $50 off any job over $250, $75 off any job over $500, $100 off any job over $750, qualifications, experience 25 years. No job is to small. Handyman service. home repair. Free estimates. Examples, Flooring, Cabinets, Decks, Odd Jobs, Carpentry, Painting, Drywall repair, Ceramic tile, Screen repair, fence repair, Pressure wash, Hang a Picture, wood rot repair, Plumbing, Electrical, Small Jobs, Install ceiling fan, replace garbage disposal, toilet repair, install new lighting, Install safety grab bars, caulk tub or Kitchen, Hang Blinds/rods, Replace a switch/outlet, Replace/adjust doors and locksets, replace faucets/sinks/vanity tops, And much more. Have a signature look, I wear a canyon rambler hat on the job, full beard, and glasses. Am looking for a caricature of that with tools as main logo which should be shown on front and the back. One year warranty, Bonded, Insured. Cash or checks

```html
<!DOCTYPE html>
<html lang="en">
<head>
<meta charset="utf-8">
<title>Merle Fixwise Handyman Postcard</title>
<link rel="stylesheet" href="https://fonts.googleapis.com/css2?family=Libre+Baskerville:wght@400;700&family=Oswald:wght@600;700&family=Arimo:wght@400;700&family=Josefin+Sans:wght@600&display=swap">
<style>
  :root {
    --stage: #000000;
    --navy: #243a80;
    --navy-deep: #1c2f6c;
    --orange: #f26a21;
    --orange-red: #e6401f;
    --yellow: #f6e23a;
    --white: #ffffff;
    --swoosh: #b9c4dc;
    --coupon-bg: #eef0f6;
    --coupon-red: #d7141e;
    --ink: #111111;
  }
  * { margin: 0; padding: 0; box-sizing: border-box; }
  html, body { width: 1200px; height: 943px; overflow: hidden; background: var(--stage); }
  body { position: relative; font-family: "Arimo", Arial, sans-serif; color: var(--white); }

  .card { position: absolute; left: 280px; width: 586px; overflow: hidden; background: var(--navy); }
  .card--front { top: 15px; height: 453px; }
  .card--back { top: 478px; height: 455px; }
  .card__bg { position: absolute; inset: 0; }

  .mascot {
    position: absolute; left: 22px; top: 20px; width: 160px; height: 330px;
    border-radius: 40% 40% 12% 12%;
    background: linear-gradient(180deg, #6b4a2c 0%, #e9b48b 22%, #3b5fbf 45%, #2f4fa8 80%, #6b4a2c 100%);
    opacity: .9;
  }

  .brand { position: absolute; font-family: "Libre Baskerville", Georgia, serif; font-weight: 700; letter-spacing: .5px; color: var(--white); white-space: nowrap; }
  .card--front .brand { left: 150px; top: 34px; font-size: 27px; }
  .tagline { position: absolute; left: 152px; top: 68px; font-family: "Libre Baskerville", Georgia, serif; font-size: 18px; color: var(--yellow); }

  .estimate-badge {
    position: absolute; left: 432px; top: 38px; width: 122px; height: 92px;
    border-radius: 46% 54% 50% 50%;
    background: radial-gradient(circle at 45% 40%, #ffffff 0 45%, #f26a21 46% 62%, #2a66c8 63% 100%);
  }

  .services__title { position: absolute; left: 183px; top: 124px; font-size: 18px; font-weight: 700; color: var(--orange); letter-spacing: .2px; }
  .services__col { position: absolute; top: 145px; list-style: none; font-size: 11px; font-weight: 700; line-height: 14px; white-space: nowrap; }
  .services__col li::before { content: "•"; color: var(--orange); margin-right: 3px; }
  .services__col--a { left: 183px; }
  .services__col--b { left: 267px; }
  .services__col--c { left: 382px; }

  .no-job { position: absolute; left: 235px; top: 285px; font-family: "Libre Baskerville", Georgia, serif; font-weight: 700; font-size: 17px; letter-spacing: .3px; }
  .call { position: absolute; left: 218px; top: 302px; display: flex; align-items: center; gap: 4px; font-family: "Oswald", Impact, sans-serif; font-weight: 700; font-size: 31px; color: var(--orange); letter-spacing: -.5px; white-space: nowrap; }
  .call svg { width: 16px; height: 30px; }

  .address { position: absolute; left: 30px; top: 381px; font-size: 14px; font-weight: 700; line-height: 16px; white-space: nowrap; }
  .address__label { color: var(--ink); font-weight: 400; }
  .email { position: absolute; display: flex; align-items: center; gap: 7px; font-size: 16px; white-space: nowrap; }
  .card--front .email { left: 262px; top: 406px; }
  .email svg { width: 22px; height: 14px; }

  .page-turn { position: absolute; right: 0; bottom: 0; width: 110px; height: 115px; }
  .page-turn__text { position: absolute; right: 12px; bottom: 28px; transform: rotate(-58deg); font-size: 9px; font-weight: 700; color: var(--ink); text-align: center; line-height: 10px; }

  .card--back .brand { left: 155px; top: 24px; font-size: 25px; }
  .back-address { position: absolute; left: 155px; top: 54px; font-size: 13px; font-weight: 700; color: var(--yellow); white-space: nowrap; }
  .experience { position: absolute; left: 177px; top: 106px; font-family: "Josefin Sans", Arial, sans-serif; font-weight: 600; font-size: 17px; letter-spacing: .3px; white-space: nowrap; }
  .experience b { font-family: "Libre Baskerville", Georgia, serif; color: var(--yellow); font-size: 24px; }

  .coupons {
    position: absolute; left: 236px; top: 148px; width: 304px; height: 196px;
    display: grid; grid-template-columns: 1fr 1fr; grid-template-rows: 1fr 1fr;
    background: var(--coupon-bg); border: 2px dashed var(--ink); outline: 3px solid var(--white);
  }
  .coupon { position: relative; display: flex; flex-direction: column; align-items: center; justify-content: center; gap: 4px; }
  .coupon:nth-child(odd) { border-right: 2px dashed var(--ink); }
  .coupon:nth-child(-n+2) { border-bottom: 2px dashed var(--ink); }
  .coupon__deal { display: flex; align-items: flex-end; font-family: "Libre Baskerville", Georgia, serif; line-height: 1; }
  .coupon__amount { font-size: 48px; color: var(--coupon-red); letter-spacing: -3px; }
  .coupon__side { display: flex; flex-direction: column; color: var(--ink); margin-left: 2px; margin-bottom: 4px; }
  .coupon__currency { font-size: 16px; font-weight: 700; }
  .coupon__off { font-size: 19px; }
  .coupon__terms { background: var(--navy-deep); color: var(--white); font-family: "Libre Baskerville", Georgia, serif; font-size: 9.5px; padding: 2px 14px; white-space: nowrap; }
  .coupon__terms b { color: var(--yellow); font-style: italic; }

  .back-call { position: absolute; left: 25px; top: 398px; font-family: "Oswald", Impact, sans-serif; font-weight: 700; font-size: 24px; letter-spacing: -.5px; white-space: nowrap; }
  .back-call span { color: var(--navy-deep); font-size: 29px; }
  .card--back .email { left: 330px; top: 411px; font-size: 15px; }
</style>
</head>
<body>

<section class="card card--front">
  <svg class="card__bg" viewBox="0 0 586 453" preserveAspectRatio="none">
    <defs>
      <linearGradient id="orangeFront" x1="0" y1="0" x2="1" y2="0">
        <stop offset="0" stop-color="#e6401f"/><stop offset="1" stop-color="#f47d22"/>
      </linearGradient>
    </defs>
    <path d="M0 272 C120 300 200 370 330 366 C430 362 500 338 586 326 L586 453 L0 453Z" fill="#ffffff"/>
    <path d="M0 284 C120 312 200 380 330 376 C430 372 500 350 586 338 L586 453 L0 453Z" fill="url(#orangeFront)"/>
    <path d="M150 128 C210 100 340 100 420 116 C330 108 230 112 150 128Z" fill="var(--swoosh)"/>
    <path d="M260 328 C240 300 400 290 540 312 C560 330 480 352 300 350 C420 346 530 330 520 316 C430 300 300 306 260 328Z" fill="var(--swoosh)"/>
  </svg>

  <div class="mascot" role="img" aria-label="Caricature of a bearded handyman in a wide-brim hat and glasses, wearing overalls, holding a toolbox and giving a thumbs up"></div>

  <h1 class="brand">MERLE FIXWISE</h1>
  <p class="tagline">Handyman Service</p>
  <div class="estimate-badge" role="img" aria-label="Free estimates badge"></div>

  <h2 class="services__title">SERVICES INCLUDES</h2>
  <ul class="services__col services__col--a">
    <li>Flooring,</li><li>Cabinets,</li><li>Decks,</li><li>Odd Jobs,</li><li>Carpentry,</li><li>Painting,</li><li>Drywall repair,</li><li>Ceramic tile,</li>
  </ul>
  <ul class="services__col services__col--b">
    <li>Screen repair,</li><li>Fence repair,</li><li>Pressure wash,</li><li>Hang a Picture,</li><li>wood rot repair,</li><li>Plumbing, Electrical,</li><li>Small Jobs,</li><li>Install ceiling fan,</li><li>Toilet repair,</li>
  </ul>
  <ul class="services__col services__col--c">
    <li>Replace garbage disposal,</li><li>Install new lighting,</li><li>Install safety grab bars,</li><li>Caulk tub or Kitchen,</li><li>Hang Blinds/rods,</li><li>Replace a switch/outlet,</li><li>Replace/adjust doors and locksets,</li><li>Replace faucets/sinks/vanity tops,</li><li>And much more</li>
  </ul>

  <p class="no-job">NO JOB IS TOO SMALL</p>
  <p class="call">
    <svg viewBox="0 0 16 30"><path d="M9 2 C3 4 1 10 1 15 C1 20 3 26 9 28 L11 23 C7 22 6 18 6 15 C6 12 7 8 11 7Z" fill="#ffffff"/></svg>
    CALL - 937-555-0148
  </p>

  <div class="address">
    <p class="address__label">Address</p>
    <p>4718 Quarry Bend Ln NW,</p>
    <p>Maple Hollow, Vermont 05999</p>
  </div>
  <p class="email">
    <svg viewBox="0 0 22 14"><rect x="1" y="1" width="20" height="12" fill="none" stroke="#1c2f6c" stroke-width="1.6"/><path d="M1 1 L11 8 L21 1" fill="none" stroke="#1c2f6c" stroke-width="1.6"/></svg>
    mtolbert@fixwisemail.com
  </p>

  <svg class="page-turn" viewBox="0 0 110 115">
    <defs>
      <linearGradient id="curlShade" x1="0" y1="0" x2="1" y2="1">
        <stop offset="0" stop-color="#f4f4f5"/><stop offset="1" stop-color="#a9abaf"/>
      </linearGradient>
    </defs>
    <path d="M110 0 L110 115 L0 115 C30 90 50 70 62 30 C70 15 90 5 110 0Z" fill="url(#curlShade)"/>
    <path d="M18 26 L34 40 L30 44 L44 46 L42 32 L38 36 L22 22Z" fill="#3c6f86"/>
  </svg>
  <p class="page-turn__text">TURN FOR<br>OFFERS</p>
</section>

<section class="card card--back">
  <svg class="card__bg" viewBox="0 0 586 455" preserveAspectRatio="none">
    <defs>
      <linearGradient id="orangeBack" x1="0" y1="0" x2="1" y2="0">
        <stop offset="0" stop-color="#e6401f"/><stop offset="1" stop-color="#f47d22"/>
      </linearGradient>
    </defs>
    <path d="M0 300 C120 330 220 368 360 368 C460 368 530 358 586 352 L586 455 L0 455Z" fill="#ffffff"/>
    <path d="M0 312 C120 342 220 380 360 380 C460 380 530 372 586 366 L586 455 L0 455Z" fill="url(#orangeBack)"/>
    <path d="M150 128 C140 100 250 84 380 92 C270 92 170 104 150 128Z" fill="var(--swoosh)"/>
  </svg>

  <div class="mascot" role="img" aria-label="Caricature of a bearded handyman in a wide-brim hat and glasses, wearing overalls, holding a toolbox and giving a thumbs up"></div>

  <h1 class="brand">MERLE FIXWISE</h1>
  <p class="back-address">4718 Quarry Bend Ln NW,Maple Hollow,Vermont 05999</p>
  <p class="experience">QUALIFICATIONS, EXPERIENCE <b>25</b> YEARS</p>

  <div class="coupons">
    <div class="coupon">
      <div class="coupon__deal"><span class="coupon__amount">25</span><span class="coupon__side"><span class="coupon__currency">$</span><span class="coupon__off">OFF</span></span></div>
      <p class="coupon__terms">Any Job Over <b>$100</b></p>
    </div>
    <div class="coupon">
      <div class="coupon__deal"><span class="coupon__amount">50</span><span class="coupon__side"><span class="coupon__currency">$</span><span class="coupon__off">OFF</span></span></div>
      <p class="coupon__terms">Any Job Over <b>$250</b></p>
    </div>
    <div class="coupon">
      <div class="coupon__deal"><span class="coupon__amount">75</span><span class="coupon__side"><span class="coupon__currency">$</span><span class="coupon__off">OFF</span></span></div>
      <p class="coupon__terms">Any Job Over <b>$500</b></p>
    </div>
    <div class="coupon">
      <div class="coupon__deal"><span class="coupon__amount">100</span><span class="coupon__side"><span class="coupon__currency">$</span><span class="coupon__off">OFF</span></span></div>
      <p class="coupon__terms">Any Job Over <b>$750</b></p>
    </div>
  </div>

  <p class="back-call">CALL TODAY - <span>937-555-0148</span></p>
  <p class="email">Email - mtolbert@fixwisemail.com</p>
</section>

</body>
</html>
```